Upscale business cards needed for Board of Directors

We need professional business cards created for members of our family business Board of Directors. We would like these relatively simple and straightforward, but also with a unique element to set them apart. Probably stick with neutral and simple colors - white, grey etc. We need space for the traditional elements, including name, title, address, email/phone number. And we will be creating several from this template so it needs to be template that is easy to switch information in and out of.
Business
See description

```html
<!DOCTYPE html>
<html lang="en">
<head>
<meta charset="utf-8">
<title>Harborline Holdings – Business Card</title>
<link rel="stylesheet" href="https://fonts.googleapis.com/css2?family=Open+Sans:wght@400;700;800&display=swap">
<style>
  :root {
    --backdrop: #b9b9b9;
    --card-dark: #343233;
    --card-light: #ffffff;
    --gold: #b09a74;
    --ink: #1f1d1e;
    --muted: #7a7a7a;
    --soft-text: #a9a7a8;
  }
  * { box-sizing: border-box; margin: 0; padding: 0; }
  html, body {
    width: 1200px; height: 1000px; overflow: hidden;
    background: var(--backdrop);
    font-family: "Open Sans", Arial, sans-serif;
  }
  .card {
    position: absolute; left: 287px; width: 626px; height: 357px;
    box-shadow: 0 4px 14px rgba(0,0,0,.35);
  }
  .card--front { top: 141px; background: var(--card-dark); }
  .card--back { top: 531px; background: var(--card-light); }

  .wordmark { font-weight: 800; text-align: center; line-height: 1; }
  .wordmark__main { display: block; letter-spacing: 0.5px; }
  .wordmark__sub { display: block; letter-spacing: 7px; }

  .card--front .wordmark {
    position: absolute; left: 0; right: 0; top: 138px; color: #fff;
  }
  .card--front .wordmark__main { font-size: 50px; }
  .card--front .wordmark__sub { font-size: 29px; margin-top: 10px; }

  .front-web {
    position: absolute; left: 0; right: 0; top: 307px;
    text-align: center; font-size: 13px; color: var(--soft-text);
  }

  .card--back .wordmark {
    position: absolute; left: 30px; width: 300px; top: 150px; color: var(--ink);
  }
  .card--back .wordmark__main { font-size: 33px; }
  .card--back .wordmark__sub { font-size: 19px; margin-top: 7px; letter-spacing: 4.5px; }

  .divider {
    position: absolute; left: 312px; top: 107px; width: 1px; height: 145px;
    background: var(--gold);
  }
  .contact { position: absolute; left: 338px; top: 106px; color: var(--muted); font-size: 13px; }
  .contact__name { font-size: 17px; font-weight: 700; color: var(--gold); line-height: 20px; }
  .contact__title { line-height: 18px; margin-bottom: 11px; }
  .contact__list { list-style: none; }
  .contact__list li { display: flex; align-items: center; gap: 6px; line-height: 18px; }
  .contact__list svg { width: 11px; height: 11px; fill: none; stroke: var(--gold); stroke-width: 1.4; }
  .contact__address { margin-top: 9px; line-height: 18px; }
</style>
</head>
<body>
  <section class="card card--front">
    <div class="wordmark">
      <span class="wordmark__main">HARBORLINE</span>
      <span class="wordmark__sub">HOLDINGS</span>
    </div>
    <p class="front-web">www.harborlineholdings.com</p>
  </section>

  <section class="card card--back">
    <div class="wordmark">
      <span class="wordmark__main">HARBORLINE</span>
      <span class="wordmark__sub">HOLDINGS</span>
    </div>
    <div class="divider"></div>
    <div class="contact">
      <p class="contact__name">Oliver Grant</p>
      <p class="contact__title">President</p>
      <ul class="contact__list">
        <li><svg viewBox="0 0 12 12"><rect x="3" y="0.8" width="6" height="10.4" rx="1"/><line x1="5" y1="9.3" x2="7" y2="9.3"/></svg>012-345-6789</li>
        <li><svg viewBox="0 0 12 12"><rect x="0.8" y="2.5" width="10.4" height="7" /><polyline points="0.8,2.5 6,6.5 11.2,2.5"/></svg>info@harborlineholdings.com</li>
        <li><svg viewBox="0 0 12 12"><circle cx="6" cy="6" r="5"/><ellipse cx="6" cy="6" rx="2.2" ry="5"/><line x1="1" y1="6" x2="11" y2="6"/></svg>www.harborlineholdings.com</li>
      </ul>
      <p class="contact__address">Street name, Suite 100 State,<br>Zip Code, Country</p>
    </div>
  </section>
</body>
</html>
```